RW Hollis LLC Business Card - Civil Engineering & Consulting Firm

We need a Business Card that is elegant, and masculine.  It is our Professional Civil Engineering & Consulting Company located in San Antonio TX (Not s construction or builder firm- no gears & no tool images please). We provide civil engineering services including  commercial site plans, grading and drainage plans, utility plans, hydraulics and hydrology, land planning, utility coordination, and other general civil engineering services related to commercial and residential development.
We have 2 existing Logos. We would like to convey reliability, strength, trustworthiness and attention to detail.  Blues and orange tones as per logo We are OK with the use of a darker blue in the mix.  We have 2 logo versions - Full Company Name Logo to go on the back of card, & Small Icon Logo for the front w/ personal Info.

Target Market(s)
Architects, Real Estate Developers, Other Strctural Engineers, Surveyers, General Contractors
Industry/Entity Type
Professional Civil Engineering
Contact Information for Business Card
Name, Position, Address, Cell & Office #, email, and company website
Font styles to use
Other font styles liked:
- Avian
Requirements
Should not have
- No Tools, No Gears, no Cranes, or Construction Equipment.

```html
<!DOCTYPE html>
<html lang="en">
<head>
<meta charset="utf-8">
<title>RW Hollis LLC Business Card</title>
<link rel="stylesheet" href="https://fonts.googleapis.com/css2?family=Josefin+Sans:wght@300;400&family=Arimo:wght@400&display=swap">
<style>
  :root {
    --backdrop: #2b2b2d;
    --card: #0d0d0e;
    --card-edge: #1a1a1c;
    --blue: #6fa8dc;
    --orange: #f0962c;
    --white: #f2f2f2;
    --muted: #d9d9d9;
    --divider: #3a3a3d;
  }
  * { margin: 0; padding: 0; box-sizing: border-box; }
  html, body {
    width: 1200px; height: 900px; overflow: hidden;
    background: var(--backdrop);
  }
  .sheet {
    position: relative; width: 1200px; height: 900px;
    display: flex; flex-direction: column; align-items: center;
    justify-content: center; gap: 40px;
  }
  .card {
    position: relative; width: 700px; height: 400px;
    background: var(--card);
    border: 1px solid var(--card-edge);
    border-radius: 22px;
    overflow: hidden;
  }

  /* Front: identity + contact */
  .card-front { display: flex; }
  .front-brand {
    width: 46%; display: flex; align-items: center; justify-content: center;
    border-right: 1px solid var(--divider);
    margin: 50px 0;
  }
  .brand-name {
    font-family: "Josefin Sans", sans-serif; font-weight: 300;
    letter-spacing: 3px; text-transform: uppercase;
    display: flex; align-items: center; gap: 14px;
  }
  .brand-mark { width: 14px; height: 14px; }
  .front-brand .brand-name { color: var(--blue); font-size: 30px; }
  .front-brand .brand-mark { background: var(--orange); }

  .front-contact {
    flex: 1; padding: 70px 0 0 44px; color: var(--white);
    font-family: "Arimo", sans-serif;
  }
  .person-name {
    font-family: "Josefin Sans", sans-serif; font-weight: 300;
    font-size: 32px; letter-spacing: 0.5px; text-transform: uppercase;
    line-height: 1;
  }
  .person-name .first { color: var(--blue); }
  .person-name .last { color: var(--orange); }
  .person-role { font-size: 17px; margin-top: 6px; color: var(--white); }

  .contact-list { list-style: none; margin-top: 22px; font-size: 17px; line-height: 1.55; }
  .contact-list li { display: flex; align-items: center; gap: 10px; }
  .contact-icon { width: 16px; height: 16px; flex: none; }
  .accent { color: var(--orange); }
  .address { margin-top: 20px; font-size: 17px; line-height: 1.4; color: var(--muted); }

  /* Back: full name + tagline */
  .card-back {
    display: flex; flex-direction: column; align-items: center; justify-content: center;
  }
  .card-back .brand-name { color: var(--white); font-size: 48px; letter-spacing: 6px; }
  .card-back .brand-mark { width: 20px; height: 20px; background: var(--white); }
  .tagline {
    margin-top: 70px;
    font-family: "Arimo", sans-serif; font-size: 16px; letter-spacing: 0.3px;
    color: var(--white); text-transform: uppercase;
  }
</style>
</head>
<body>
<main class="sheet">
  <section class="card card-front">
    <div class="front-brand">
      <div class="brand-name"><span class="brand-mark"></span>RW Hollis LLC</div>
    </div>
    <div class="front-contact">
      <h1 class="person-name"><span class="first">Daniel</span> <span class="last">Marsh</span></h1>
      <p class="person-role">Managing Director</p>
      <ul class="contact-list">
        <li>
          <svg class="contact-icon" viewBox="0 0 16 16" aria-hidden="true"><path d="M4 1.5l2.2 2.8-1.3 1.6c.8 1.9 2.3 3.4 4.2 4.2l1.6-1.3 2.8 2.2-1.2 2.2C7 13 3 9 1.8 3.2z" fill="var(--blue)"/></svg>
          044-555 010 246
        </li>
        <li>
          <svg class="contact-icon" viewBox="0 0 16 16" aria-hidden="true"><rect x="1" y="3.5" width="14" height="9" fill="var(--blue)"/><path d="M1 3.5l7 5 7-5" fill="none" stroke="var(--card)" stroke-width="1.2"/></svg>
          info@hollisce.com
        </li>
        <li>
          <svg class="contact-icon" viewBox="0 0 16 16" aria-hidden="true"><g fill="none" stroke="var(--blue)" stroke-width="1.3"><circle cx="8" cy="8" r="6.5"/><ellipse cx="8" cy="8" rx="2.8" ry="6.5"/><path d="M1.5 8h13M2.6 4.8h10.8M2.6 11.2h10.8"/></g></svg>
          www.<span class="accent">hollisce</span>.com
        </li>
      </ul>
      <p class="address">421, Address line goes here<br>45452, Country Name</p>
    </div>
  </section>

  <section class="card card-back">
    <div class="brand-name"><span class="brand-mark"></span>RW Hollis LLC</div>
    <p class="tagline">Commercial and Residential Development</p>
  </section>
</main>
</body>
</html>
```